Wohnhof am Weiher - Zeitungsinserat für den Verkauf von Eigentumswohnungen

Wir brauchen ein Zeitungsinserat in zwei Formaten. Einmal 296 Breite x 440 Höhe mm und einmal 296 Breite x 220 mm Höhe.
Als Basis dient der sehr grobe Entwurf im Powerpoint (Entwurf.pptx).
Auf dem Entwurf fehlen noch die Kontaktangeben:
Brunnhofer Liegenschaften AG
Seematteweg 14
4387 Tannried
079 462 37 58
rbrunnhofer@tessin-ostwald.ch

Zudem muss noch der Link auf die Webseite aufgeführt werden.
www.wohnhof-am-weiher.ch

Zudem fehlt noch der Text:
Fordern Sie noch heute die Verkaufsunterlagen gedruckt oder per Email an. Schreiben Sie uns einfach eine Chatpost mit Ihrer Adresse.

Ich habe noch Files von den Innenvisualisierungen, den Aussenvisualisierungen sowie unser Logo hinzugefügt. Zudem habe ich Ihnen die Verkaufsbrochure angefügt. Sie können die Daten vom Entwurf gerne ergänzen wenn Ihnen etwas gefällt. Schön wäre es, wenn Sie den Stil ähnlich machen würden wie die Brochure.

Target Market(s)

Famillien, Paare und Rentner

Font styles to use
Serif

Colors

Designer to choose colors to be used in the design.

Requirements
Must have
• Tolles Design das sofort anspricht!

```html
<!DOCTYPE html>
<html lang="de">
<head>
<meta charset="utf-8">
<title>Wohnhof am Weiher – Inserat</title>
<link href="https://fonts.googleapis.com/css2?family=Crimson+Text:wght@400;600;700&family=Roboto:wght@400&display=swap" rel="stylesheet">
<style>
  :root{
    --board:#c6c7c7;
    --paper:#ffffff;
    --blue:#0f6a93;
    --blue-dark:#0a4e6e;
    --red:#d3202f;
    --ink:#2c2c2c;
    --rule:#8a8a8a;
    --serif:"Crimson Text", Georgia, serif;
  }
  *{box-sizing:border-box;margin:0;padding:0}
  html,body{width:831px;height:1200px;overflow:hidden;background:var(--board)}
  .canvas{position:relative;width:831px;height:1200px;background:var(--board);font-family:var(--serif);color:var(--ink)}
  .format-label{position:absolute;left:44px;top:36px;font-family:Roboto, Arial, sans-serif;font-size:14.5px;color:#333}
  .sheet{position:absolute;left:45px;top:59px;width:740px;height:1101px;background:var(--paper);overflow:hidden}
  .hero{position:absolute;left:0;top:0;width:740px;height:431px;
    clip-path:polygon(0 61%,28% 0,40% 0,100% 44%,100% 100%,0 100%);
    background:
      radial-gradient(ellipse 22% 30% at 8% 92%, rgba(46,92,28,.75), rgba(46,92,28,0) 100%),
      radial-gradient(ellipse 14% 36% at 84% 42%, rgba(70,112,48,.6), rgba(70,112,48,0) 100%),
      linear-gradient(180deg,
        #9fbddc 0%, #c4d7ea 22%, #e3ebf2 38%,
        #d9dbd6 44%, #c9cac4 55%, #b4b7ae 64%, #8aa866 70%,
        #79a04a 74%, #bfc3c3 75.5%, #c9cccc 79%, #7fa54d 80.5%,
        #679a3a 88%, #4f8430 100%)}
  .banner{position:absolute;left:45px;top:116px;width:530px;height:112px}
  .title{position:absolute;left:45px;width:570px;text-align:center;color:#fff}
  .title h1{position:absolute;top:118px;left:0;width:100%;font-size:43px;font-weight:400;letter-spacing:.3px;line-height:1}
  .title p{position:absolute;top:166px;left:0;width:100%;font-size:17px;line-height:1}
  .house-tag{position:absolute;font-size:9px;font-weight:700;color:var(--red)}
  .house-tag svg{position:absolute;left:0;top:-10px;width:32px;height:22px}
  .house-tag span{position:relative;left:1px;top:2px}
  .block-title{position:absolute;font-size:20px;font-weight:700;color:var(--red);line-height:1}
  .visual{position:absolute;width:143px;height:89px;
    background:
      linear-gradient(180deg, rgba(255,255,255,0) 60%, rgba(150,140,128,.35) 100%),
      linear-gradient(100deg,#f4f3f1 0%,#e6e2dc 40%,#d3cdc4 70%,#b6ab9c 100%)}
  .visual.dusk{background:
      linear-gradient(180deg, rgba(255,255,255,0) 55%, rgba(120,110,98,.35) 100%),
      linear-gradient(100deg,#e9e7e3 0%,#dcd4c8 45%,#c4b8a6 75%,#a89a86 100%)}
  .units{position:absolute;border-collapse:collapse;font-size:8.3px;line-height:11.5px}
  .units td{padding:3px 3px 2px;vertical-align:top;white-space:nowrap}
  .units td+td{border-left:0.8px solid var(--rule)}
  .units tr+tr td{border-top:0.8px solid var(--rule)}
  .units tr.tall td{height:28px}
  .location{position:absolute;left:435px;top:734px;width:350px;height:426px;background:var(--blue);color:#fff}
  .perk{position:absolute;left:19px;width:320px}
  .perk svg{position:absolute;left:0;top:0;width:16px;height:16px}
  .perk h3{margin-left:22px;font-size:13.5px;font-weight:600;letter-spacing:.4px;line-height:19px;text-transform:uppercase}
  .perk p{margin-left:22px;margin-top:3px;font-size:8.4px;line-height:12px}
  .brand{position:absolute;left:76px;top:1077px;font-size:14px;font-weight:700;color:var(--blue);line-height:16px;letter-spacing:.6px}
  .contact{position:absolute;left:239px;top:1047px;font-size:8.4px;line-height:13.5px;list-style:none}
  .contact li{position:relative;padding-left:16px}
  .contact svg{position:absolute;left:0;top:3px;width:9px;height:9px}
  .contact .tel{font-weight:700}
  .callout{position:absolute;left:67px;top:1133px;width:350px;height:15px;background:var(--red);transform:skewX(-8deg)}
  .callout p{transform:skewX(8deg);color:#fff;font-size:7.8px;font-weight:700;line-height:15px;text-align:center;white-space:nowrap}
</style>
</head>
<body>
<div class="canvas">
  <div class="format-label">Dimension - 296 x 440mm</div>

  <div class="sheet">
    <div class="hero" role="img" aria-label="Aussenvisualisierung der drei Wohnhäuser mit Garten, Weg und Bäumen"></div>
  </div>

  <svg class="banner" viewBox="0 0 530 112" aria-hidden="true">
    <polygon points="0,82 25,110 40,82" fill="var(--blue-dark)"/>
    <polygon points="66,0 524,0 478,82 0,82" fill="var(--blue)"/>
  </svg>
  <div class="title">
    <h1>Wohnhof am Weiher</h1>
    <p>Hochwertige und moderne Eigentumswohnungen</p>
  </div>

  <div class="house-tag" style="left:207px;top:236px">
    <svg viewBox="0 0 32 22"><polyline points="1,8 16,1 31,8 31,20" fill="none" stroke="var(--blue)" stroke-width="1.2"/></svg>
    <span>Haus C</span></div>
  <div class="house-tag" style="left:473px;top:273px">
    <svg viewBox="0 0 32 22"><polyline points="1,8 16,1 31,8 31,20" fill="none" stroke="var(--blue)" stroke-width="1.2"/></svg>
    <span>Haus B</span></div>
  <div class="house-tag" style="left:726px;top:262px">
    <svg viewBox="0 0 32 22"><polyline points="1,8 16,1 31,8 31,20" fill="none" stroke="var(--blue)" stroke-width="1.2"/></svg>
    <span>Haus A</span></div>

  <!-- Haus A -->
  <div class="block-title" style="left:104px;top:508px">Haus A</div>
  <div class="visual" style="left:106px;top:528px" role="img" aria-label="Innenvisualisierung Küche und Essbereich Haus A"></div>
  <div class="visual" style="left:254px;top:528px" role="img" aria-label="Innenvisualisierung Wohn- und Essbereich Haus A"></div>
  <table class="units" style="left:102px;top:631px">
    <tr><td style="width:63px">Attika Wohnung</td><td style="width:50px">4.5 Zimmer</td><td style="width:32px">108 m²</td><td style="width:97px">105 m² Sonnenterrasse</td><td>945’000 CHF</td></tr>
    <tr><td>Obergeschoss</td><td>3.5 Zimmer</td><td>81 m²</td><td>16 m²&nbsp; Balkon</td><td>754’800 CHF</td></tr>
    <tr><td>Obergeschoss</td><td>4.5 Zimmer</td><td>102 m²</td><td>33 m²&nbsp; Balkon</td><td>640’000 CHF</td></tr>
    <tr class="tall"><td>Erdgeschoss</td><td>3.5 Zimmer</td><td>81 m²</td><td>16 m²&nbsp; gedeckter Sitzplatz<br>und eigener Garten</td><td>657’000 CHF</td></tr>
    <tr class="tall"><td>Erdgeschoss</td><td>4.5 Zimmer</td><td>102 m²</td><td>33 m²&nbsp; gedeckter Sitzplatz<br>und eigener Garten</td><td>765’000 CHF</td></tr>
  </table>

  <!-- Haus B -->
  <div class="block-title" style="left:449px;top:508px">Haus B</div>
  <div class="visual" style="left:450px;top:527px;height:85px" role="img" aria-label="Innenvisualisierung Wohnbereich mit Küche Haus B"></div>
  <div class="visual dusk" style="left:598px;top:524px;height:88px" role="img" aria-label="Innenvisualisierung Wohnzimmer Haus B"></div>
  <table class="units" style="left:449px;top:627px">
    <tr><td style="width:63px">Attika Wohnung</td><td style="width:49px">4.5 Zimmer</td><td style="width:33px">109 m²</td><td style="width:97px">107 m² Sonnenterrasse</td><td>965’000 CHF</td></tr>
    <tr><td>Obergeschoss</td><td>2.5 Zimmer</td><td>69 m²</td><td>14 m²&nbsp; Balkon</td><td>550’000 CHF</td></tr>
    <tr><td>Obergeschoss</td><td>4.5 Zimmer</td><td>117 m²</td><td>42 m²&nbsp; Balkon</td><td>877’500 CHF</td></tr>
    <tr class="tall"><td>Erdgeschoss</td><td>2.5 Zimmer</td><td>69 m²</td><td>14 m²&nbsp; gedeckter Sitzplatz<br>und eigener Garten</td><td>560’000 CHF</td></tr>
    <tr class="tall"><td>Erdgeschoss</td><td>4.5 Zimmer</td><td>117 m²</td><td>42 m²&nbsp; gedeckter Sitzplatz<br>und eigener Garten</td><td>889’000 CHF</td></tr>
  </table>

  <!-- Haus C -->
  <div class="block-title" style="left:105px;top:763px">Haus C</div>
  <div class="visual" style="left:105px;top:789px" role="img" aria-label="Innenvisualisierung Küche Haus C"></div>
  <div class="visual dusk" style="left:252px;top:789px" role="img" aria-label="Innenvisualisierung Wohn- und Essbereich Haus C"></div>
  <table class="units" style="left:102px;top:888px">
    <tr><td style="width:63px">Attika Wohnung</td><td style="width:49px">4.5 Zimmer</td><td style="width:32px">129 m²</td><td style="width:96px">132 m² Sonnenterrasse</td><td>1’125’000 CHF</td></tr>
    <tr><td>Obergeschoss</td><td>5.5 Zimmer</td><td>143 m²</td><td>43 m²&nbsp; Balkon</td><td>1’058’000 CHF</td></tr>
    <tr><td>Obergeschoss</td><td>3.5 Zimmer</td><td>96 m²</td><td>23 m²&nbsp; Balkon</td><td>730’000 CHF</td></tr>
    <tr class="tall"><td>Erdgeschoss</td><td>5.5 Zimmer</td><td>143 m²</td><td>43 m²&nbsp; gedeckter Sitzplatz<br>und eigener Garten</td><td>1’065’000 CHF</td></tr>
    <tr class="tall"><td>Erdgeschoss</td><td>3.5 Zimmer</td><td>96 m²</td><td>23 m²&nbsp; gedeckter Sitzplatz<br>und eigener Garten</td><td>740’000 CHF</td></tr>
  </table>

  <!-- Lage -->
  <section class="location">
    <div class="perk" style="top:14px">
      <svg viewBox="0 0 16 16"><circle cx="8" cy="8" r="7" fill="none" stroke="#fff" stroke-width="1.3"/><polyline points="4.5,8.2 7,10.5 11.5,5.5" fill="none" stroke="#fff" stroke-width="1.4"/></svg>
      <h3>Bus und Bahn</h3>
      <p>Der Bahnhof von Mühlau mit Zugverbindungen nach Rheinfeld (20 Minuten) und Sorvilier ist in wenigen Minuten mit dem Bus zu erreichen.</p>
    </div>
    <div class="perk" style="top:76px">
      <svg viewBox="0 0 16 16"><circle cx="8" cy="8" r="7" fill="none" stroke="#fff" stroke-width="1.3"/><polyline points="4.5,8.2 7,10.5 11.5,5.5" fill="none" stroke="#fff" stroke-width="1.4"/></svg>
      <h3>Rheinfeld – Stadt</h3>
      <p>Der nahegelegene Bahnhof in Mühlau verfügt über sehr gute Verbindungen nach Rheinfeld (20 Minuten), welche durch den Doppelspurausbau in den kommenden Jahren sogar noch weiter verbessert werden</p>
    </div>
    <div class="perk" style="top:151px">
      <svg viewBox="0 0 16 16"><circle cx="8" cy="8" r="7" fill="none" stroke="#fff" stroke-width="1.3"/><polyline points="4.5,8.2 7,10.5 11.5,5.5" fill="none" stroke="#fff" stroke-width="1.4"/></svg>
      <h3>Autobahn</h3>
      <p>Die Wohnsiedlung ist ideal auch für den Individualverkehr erschlossen. Die Entfernung zur Autobahn A18 beträgt 12km und ist über Eichmatt innerhalb von 15 Minuten erreichbar.</p>
    </div>
    <div class="perk" style="top:223px">
      <svg viewBox="0 0 16 16"><circle cx="8" cy="8" r="7" fill="none" stroke="#fff" stroke-width="1.3"/><polyline points="4.5,8.2 7,10.5 11.5,5.5" fill="none" stroke="#fff" stroke-width="1.4"/></svg>
      <h3>Einkaufen und weitere<br>Dienstleistungen</h3>
      <p>Durch die Nähe der Gemeindegrenze zwischen Mühlau und Tannried liegen die Dorfzentren mit ihren Einkaufsmöglichkeiten (z.B. Talmarkt Center Mühlau sowie der Altstadt in Mühlau) und Dienstleistungsangeboten in max. 2 Minuten Fahrtzeit oder in 10-15 Minuten Gehdistanz.</p>
    </div>
    <div class="perk" style="top:330px">
      <svg viewBox="0 0 16 16"><circle cx="8" cy="8" r="7" fill="none" stroke="#fff" stroke-width="1.3"/><polyline points="4.5,8.2 7,10.5 11.5,5.5" fill="none" stroke="#fff" stroke-width="1.4"/></svg>
      <h3>Erholung im Grünen</h3>
      <p>Tannried erfüllt mit seinen Wäldern, dem eigenen «Weiherberg» dem «Hochkopf», den offenen Feldern, den Wander- und Velorouten und der ländlichen Ruhe alle Voraussetzungen, die ein Naherholungsgebiet begehrt machen.</p>
    </div>
  </section>

  <!-- Anbieter -->
  <div class="brand">Brunnhofer<br>Liegenschaften AG</div>
  <ul class="contact">
    <li><svg viewBox="0 0 10 10"><circle cx="5" cy="5" r="5" fill="var(--blue)"/><circle cx="5" cy="4.2" r="1.5" fill="#fff"/></svg>Brunnhofer Liegenschaften AG Seematteweg 14<br>4387 Tannried</li>
    <li class="tel"><svg viewBox="0 0 10 10"><circle cx="5" cy="5" r="5" fill="var(--blue)"/><rect x="3.5" y="2.3" width="3" height="5.4" rx=".6" fill="#fff"/></svg>079 462 37 58</li>
    <li><svg viewBox="0 0 10 10"><circle cx="5" cy="5" r="5" fill="var(--blue)"/><rect x="2.5" y="3.3" width="5" height="3.4" fill="#fff"/></svg>rbrunnhofer@tessin-ostwald.ch</li>
    <li><svg viewBox="0 0 10 10"><circle cx="5" cy="5" r="5" fill="var(--blue)"/><circle cx="5" cy="5" r="2.6" fill="none" stroke="#fff" stroke-width=".8"/><line x1="2.4" y1="5" x2="7.6" y2="5" stroke="#fff" stroke-width=".7"/></svg>www.wohnhof-am-weiher.ch</li>
  </ul>

  <div class="callout"><p>Verkaufsunterlagen noch heute gedruckt oder per Email anfordern – per Chatpost mit Ihrer Adresse.</p></div>
</div>
</body>
</html>
```